Flyer für ambulanten Pflegedienst
Zielgruppe
Ambulanter Pflegedienst in Gründung. Habe schon ein Logo und Text. Zielgruppe sind Pflege und Hilfsbedürftige Menschen

```html
<!DOCTYPE html>
<html lang="de">
<head>
<meta charset="utf-8">
<title>Sonnweg Pflege – Flyer</title>
<link rel="stylesheet" href="https://fonts.googleapis.com/css2?family=Arimo:wght@400;700&family=Libre+Baskerville:wght@400&display=swap">
<style>
:root{
  --teal:#3a9dbd;
  --stage:#86bccb;
  --paper:#ffffff;
  --ink:#3b3b3b;
}
*{box-sizing:border-box;margin:0;padding:0}
html,body{width:750px;height:1200px;overflow:hidden;background:var(--stage)}
body{font-family:"Arimo",Arial,sans-serif;color:var(--ink);position:relative}
.page{position:absolute;left:175px;width:400px;height:578px;background:var(--paper);overflow:hidden;padding:0 34px}
.page--front{top:12px}
.page--back{top:610px;padding-top:28px}
.serif{font-family:"Libre Baskerville",Georgia,serif;font-weight:400;color:var(--teal)}
.wordmark{font-family:"Arimo",Arial,sans-serif;font-weight:700;color:var(--ink);white-space:nowrap}
.wordmark--top{display:block;text-align:center;font-size:20px;margin-top:44px}
.h1{font-size:18px;margin-top:44px;margin-bottom:9px}
.copy{font-size:7.3px;line-height:1.42;margin-bottom:8px}
.hl{color:var(--teal);font-weight:700}
.lead{font-size:7.3px;font-weight:700;color:var(--teal);margin-bottom:4px}
.bullets{display:grid;grid-template-columns:124px 1fr;font-size:7.1px;line-height:1.42;list-style:none;padding-left:10px}
.bullets li::before{content:"•";margin-right:6px}
.h2{font-size:18px;margin-top:24px;margin-bottom:8px}
.service{display:flex;gap:12px;margin-bottom:12px;align-items:flex-start}
.service__icon{flex:0 0 35px;height:35px;border-radius:50%;background:var(--teal);display:flex;align-items:center;justify-content:center;margin-top:10px;color:#fff;font-weight:700;font-size:11px}
.service__title{font-size:9.4px;margin-bottom:3px}
.service__text{font-size:5.6px;line-height:1.4}
.service__text b{font-weight:700}
.back-copy{font-size:7.1px;line-height:1.42;margin:6px 0 8px}
.steps{list-style:none}
.step{display:flex;gap:12px;margin-bottom:7px}
.step__num{flex:0 0 12px;height:12px;border-radius:50%;background:var(--teal);color:#fff;font-size:6px;font-weight:700;display:flex;align-items:center;justify-content:center;margin-top:2px}
.step__title{font-size:5.8px;font-weight:700}
.step__text{font-size:5.5px;line-height:1.38}
.contact{position:absolute;left:0;bottom:0;width:235px;height:63px;background:var(--teal);border-top-right-radius:12px;color:#fff;padding:9px 0 0 35px}
.contact__title{font-family:"Libre Baskerville",Georgia,serif;font-size:8.6px;margin-bottom:5px}
.contact__row{display:flex;align-items:center;gap:9px;font-size:10px;line-height:1.35}
.wordmark--bottom{position:absolute;right:30px;bottom:26px;font-size:13px}
</style>
</head>
<body>

<section class="page page--front">
  <span class="wordmark wordmark--top">Sonnweg Pflege</span>

  <h1 class="h1 serif">Wir bei Sonnweg Pflege</h1>
  <p class="copy">Uns liegt es am Herzen durch qualitativ hochwertige und individuelle Unterstützungsleistungen den Menschen ein selbstbestimmtes Leben zu ermöglichen. Wir setzen auf Fachkompetenz und Empathie, um sicherzustellen, dass unsere Kunden die bestmögliche medizinische Versorgung erhalten.</p>
  <p class="copy">Unsere Dienstleistung umfasst die <span class="hl">ambulante Pflege gemäß SGB XI sowie die Behandlungspflege</span> gemäß SGB V. Betreuungs- und Entlastungszeiten nach § 45 SGB XI um Menschen im Alltag zu unterstützen und ihre Lebensqualität zu steigern.</p>
  <p class="copy">Pflegebedürftig ist, wer aufgrund einer Körperlichen, geistigen oder seelischen Krankheit bzw. Behinderung in erheblichen Umfang Hilfe bis hin zur vollumfänglichen Betreuung benötigt.</p>
  <p class="lead">Die Leistungen des Altenpflege- und Seniorenbetreuungsdienstes erstrecken sich auf die</p>
  <ul class="bullets">
    <li>Grundpflege</li><li>hauswirtschaftliche Versorgung</li>
    <li>Behandlungspflege</li><li>Verhinderungspflege</li>
    <li>24-Stundenpflege</li><li>Alltagsbegleitung</li>
    <li>ambulante Palliativ Pflege</li>
  </ul>

  <h2 class="h2 serif">Unsere Leistungen</h2>

  <div class="service">
    <div class="service__icon">
      <svg width="18" height="18" viewBox="0 0 18 18" fill="#fff"><path d="M4 9a5 5 0 0 1 10 0z"/><rect x="8.2" y="2" width="1.6" height="3"/><circle cx="5" cy="12" r=".9"/><circle cx="9" cy="12" r=".9"/><circle cx="13" cy="12" r=".9"/><circle cx="7" cy="15" r=".9"/><circle cx="11" cy="15" r=".9"/></svg>
    </div>
    <div>
      <h3 class="service__title serif">Grundpflege</h3>
      <p class="service__text"><b>In der Grundpflege werden die Pflegepersonen in der Verrichtung alltäglicher Grundverrichtungen unterstützt. z.B.:</b> Duschen, Baden, Zahnpflege, Kämmen, Rasieren, An- und Auskleiden, Hilfsmittelversorgung, Mobilisation, Prophylaxen, Nahrungsaufnahme, Toilettengang u.s.w..</p>
    </div>
  </div>

  <div class="service">
    <div class="service__icon">
      <svg width="20" height="20" viewBox="0 0 20 20" fill="none" stroke="#fff" stroke-width="1.5"><path d="M7.5 2.5h5v5h5v5h-5v5h-5v-5h-5v-5h5z"/></svg>
    </div>
    <div>
      <h3 class="service__title serif">Behandlungspflege</h3>
      <p class="service__text"><b>Die Behandlungspflege umfasst alle Pflegedienste, die auf ärztlicher Verordnung hin vom Pflegepersonal durchgeführt werden, z.B.</b> Pulsmessung, Blutdruckmessung, Blutzuckermessung, Wundversorgung, Verbandswechsel, Injektionen (z.B. Insulin), Stellen der Medikamente, Anlegen von Kompressionsverbänden, An- und Ausziehen von Kompressionsstrümpfen u.s.w..</p>
    </div>
  </div>

  <div class="service">
    <div class="service__icon">24h</div>
    <div>
      <h3 class="service__title serif">24- Stunden Pflege</h3>
      <p class="service__text"><b>In verschiedenen Situationen ist die stundenweise Pflege nicht ausreichend, z.B. in der Folgezeit eines Krankenhausaufenthaltes. Es wird eine 24-Stunden-Pflege angeboten, im Rahmen derer das Pflegepersonal rund um die Uhr erreichbar ist. Typische Leistungen sind:</b> Überwachung der Vitalsituation des Patienten, Verabreichung von Medikamenten, Wundversorgung, Verbandswechsel Katheterversorgung u.s.w..</p>
    </div>
  </div>
</section>

<section class="page page--back">
  <div class="service">
    <div class="service__icon">
      <svg width="16" height="16" viewBox="0 0 16 16" fill="none" stroke="#fff" stroke-width="1.4"><path d="M3 6h10l-1.5 8h-7z"/><path d="M5 6a3 3 0 0 1 6 0"/><circle cx="11.5" cy="2.5" r="1"/></svg>
    </div>
    <div>
      <h3 class="service__title serif">Hauswirtschaftliche Versorgung</h3>
      <p class="service__text"><b>In der hauswirtschaftlichen Versorgung werden sämtliche hauswirtschaftlichen Tätigkeiten übernommen, z.B.</b> Einkaufen, Besorgungen, Zubereitung von Mahlzeiten, Abwaschen, Wäsche waschen, Bügeln, Reinigungsarbeiten (Aufräumen, Toilette, Bad, Küche, Wohn- und Schlafbereich, Staubsaugen, Staubwischen), Betreuung von Haustieren, Heizen der Wohnung (Holz, Kohle, Öl), Fahrdienste</p>
    </div>
  </div>

  <div class="service">
    <div class="service__icon">
      <svg width="16" height="18" viewBox="0 0 16 18" fill="none" stroke="#fff" stroke-width="1.3"><rect x="2.5" y="1.5" width="11" height="15" rx="1"/><path d="M5 6h6M5 9h6M5 12h6"/></svg>
    </div>
    <div>
      <h3 class="service__title serif">Betreuungs- und Entlastungsleistungen nach § 45 SGB XI</h3>
      <p class="service__text"><b>Voraussetzung ist das Vorliegen eines Pflegegrads. Bei der Antragstellung eines Pflegegrades sind wir behilflich und begleiten die Begutachtung durch den Medizinischen Dienst der Krankenkassen.</b> Unterstützung bei der Haushaltsführung, Einkaufen, Begleitung zu Ärzten, Arzttermine vereinbaren, Unterstützung beim Ausfüllen von Formularen und Anträgen, Unterstützung beim Ausfüllen von Formularen und Anträgen, Spaziergänge</p>
    </div>
  </div>

  <div class="service">
    <div class="service__icon">
      <svg width="18" height="18" viewBox="0 0 18 18" fill="#fff"><path d="M2 10l3-1 3 1 6-5c1-.8 2.5-.5 2 .5l-5 5 1 5-1.5.5-2-4-3 2v2l-1 .5-1-3-3-1z"/></svg>
    </div>
    <div>
      <h3 class="service__title serif">Verhinderungspflege</h3>
      <p class="service__text"><b>Angebot im Bereich Verhinderungspflege richtet sich an die Angehörigen, die bei der Pflege eine stundenweise Entlastung benötigen. Typische Anlässe sind z.B.</b> Urlaub, Krankheit, Überlastung</p>
    </div>
  </div>

  <div class="service">
    <div class="service__icon">
      <svg width="18" height="18" viewBox="0 0 18 18" fill="none" stroke="#fff" stroke-width="1.4"><path d="M3 3l12 12M15 3L3 15"/><circle cx="4" cy="14" r="1.6"/><circle cx="14" cy="14" r="1.6"/></svg>
    </div>
    <div>
      <h3 class="service__title serif">Alltagsbegleitung</h3>
      <p class="service__text"><b>In der Alltagsbegleitung werden die Pflegepersonen in allen alltäglichen Tätigkeiten und Freizeitaktivitäten unterstützt und begleitet. Typische Leistungen sind z.B.</b> Arztbesuche Behördengänge, Kulturelle Veranstaltungen, Spaziergänge, Ausflüge, Wanderungen, Stadtbummel, Restaurantbesuche, Friseurbesuche, Gedächtnistraining u.s.w..</p>
    </div>
  </div>

  <p class="back-copy">Der Altenpflege- und Seniorenbetreuungsdienst führt sämtliche Pflegeleistungen <span class="hl">kompetent, professionell und zuverlässig</span> aus. Das oberste Ziel der Pflege ist die Sicherung und Verbesserung der Lebensqualität und das Bewahren des gewohnten Lebensumfelds der Pflegepersonen. Krankenhaus- und Betreuungsheimaufenthalte sollen möglichst vermieden werden. Diesem Grundgedanken liegt die Erkenntnis zu Grunde, dass <span class="hl">in einer vertrauten Umgebung Kranke oft schneller gesünder werden und gerade ältere Menschen sich zu Hause besonders wohl und geborgen fühlen.</span></p>
  <p class="back-copy">Der grundlegende Geschäftsprozess des Unternehmens gliedert sich in die Bereiche Beratung, Pflegekonzept, Vertragsabschluss und Pflege:</p>

  <ol class="steps">
    <li class="step"><span class="step__num">1</span><div><div class="step__title">Beratung</div><p class="step__text">Kunden werden ausführlich unter Berücksichtigung ihrer Wünsche und Vorstellungen beraten. Denn das vorhandene Pflegeangebot bietet eine Vielzahl an Möglichkeiten. Wichtig ist der Aufbau von Vertrauen.</p></div></li>
    <li class="step"><span class="step__num">2</span><div><div class="step__title">Pflegekonzept</div><p class="step__text">Unter Berücksichtigung aller Möglichkeiten und Patientenwünsche wird ein individuelles Leistungskonzept entwickelt und eine verbindliche Kostenaufstellung erstellt.</p></div></li>
    <li class="step"><span class="step__num">3</span><div><div class="step__title">Vertragsschluss</div><p class="step__text">Alle Aufträge mit Kunden werden in schriftlicher Form geschlossen und beidseitig unterzeichnet.</p></div></li>
    <li class="step"><span class="step__num">4</span><div><div class="step__title">Pflege</div><p class="step__text">Die vereinbarten Pflegeleistungen werden nun umgesetzt. Dabei kann der Kunde stets eine hohe Ausführungsqualität erwarten. Es wird für jeden Kunden eine Mappe zur Pflegedokumentation geführt (Pflegesoftware, die stets vom Kunden sowie seinen Angehörigen eingesehen werden kann).</p></div></li>
  </ol>

  <div class="contact">
    <p class="contact__title">Melden Sie sich gerne jederzeit bei uns!</p>
    <p class="contact__row">
      <svg width="9" height="9" viewBox="0 0 10 10" fill="#fff"><path d="M2 .5l2 2-1 1.3a6 6 0 0 0 3.2 3.2L7.5 6l2 2-1.3 1.5C4.5 9.8.2 5.5.5 1.8z"/></svg>
      05678 / 98 76 54
    </p>
    <p class="contact__row">
      <svg width="9" height="8" viewBox="0 0 10 8" fill="none" stroke="#fff" stroke-width="1"><rect x=".5" y=".5" width="9" height="7"/><path d="M.5 .5l4.5 4 4.5-4"/></svg>
      info@sonnweg-pflege.de
    </p>
  </div>

  <span class="wordmark wordmark--bottom">Sonnweg Pflege</span>
</section>

</body>
</html>
```